"Harrow Crest Builders" is a residential building company and needs a new business card design and may re

We would like a redesign based on the existing logo, and would like to see a new font as well. We are bespoke home builders who build sustainable energy efficient homes.

Industry/Entity Type

Construction

Contact Information for Business Card

Business card size 40mm x 90mm

Colors

Designer to choose colors to be used in the design.

```html
<!DOCTYPE html>
<html lang="en">
<head>
<meta charset="utf-8">
<title>Harrow Crest Builders – Business Card</title>
<link href="https://fonts.googleapis.com/css2?family=Quicksand:wght@400;700&family=Cabin:wght@400&display=swap" rel="stylesheet">
<style>
  :root {
    --page-bg: #e8e5df;
    --card-white: #ffffff;
    --card-edge-grey: #e2e2e2;
    --card-dark: #262626;
    --card-darker: #181818;
    --ink: #2a2a2a;
    --ink-soft: #3c3c3c;
    --leaf: #a8c83a;
    --light-type: #e6e6e6;
  }
  * { box-sizing: border-box; margin: 0; padding: 0; }
  html, body {
    width: 1200px; height: 960px; overflow: hidden;
    background: var(--page-bg);
  }
  .canvas { position: relative; width: 1200px; height: 960px; }

  .card {
    position: absolute; left: 217px; width: 768px; height: 339px;
  }
  .card-front {
    top: 121px;
    background: radial-gradient(ellipse 75% 120% at 40% 60%, var(--card-white) 60%, var(--card-edge-grey) 100%);
  }
  .card-back {
    top: 525px;
    background: linear-gradient(180deg, var(--card-dark) 0%, var(--card-darker) 100%);
    display: flex; align-items: center; justify-content: center;
  }

  .holder-name {
    position: absolute; left: 27px; top: 30px;
    font-family: "Quicksand", sans-serif; font-size: 29px; font-weight: 400;
    color: var(--ink); line-height: 1.1;
  }
  .holder-name .surname { font-weight: 700; }
  .holder-phone {
    position: absolute; left: 27px; top: 67px;
    font-family: "Cabin", sans-serif; font-size: 25px; color: var(--ink-soft);
  }

  .brand {
    display: flex; align-items: center; gap: 12px;
    font-family: "Quicksand", sans-serif; font-weight: 400;
  }
  .brand-mark { background: var(--leaf); flex: none; }
  .brand-front { position: absolute; right: 28px; top: 50px; color: var(--ink); font-size: 28px; }
  .brand-front .brand-mark { width: 22px; height: 22px; }
  .brand-back { color: var(--light-type); font-size: 50px; gap: 20px; }
  .brand-back .brand-mark { width: 38px; height: 38px; }

  .contact-list {
    position: absolute; left: 27px; top: 178px; list-style: none;
    font-family: "Cabin", sans-serif; font-size: 19px; color: var(--ink);
  }
  .contact-list li { display: flex; align-items: center; height: 36px; }
  .contact-icon { width: 22px; height: 22px; margin-right: 9px; flex: none; }

  .registration {
    position: absolute; left: 27px; top: 293px;
    font-family: "Cabin", sans-serif; font-size: 19px; color: var(--leaf);
  }
</style>
</head>
<body>
<main class="canvas">
  <section class="card card-front" aria-label="Business card front">
    <p class="holder-name">Daniel <span class="surname">Marsh</span></p>
    <p class="holder-phone">0412 358 907</p>

    <div class="brand brand-front">
      <span class="brand-mark"></span>
      <span class="brand-name">Harrow Crest Builders</span>
    </div>

    <ul class="contact-list">
      <li>
        <svg class="contact-icon" viewBox="0 0 22 22" aria-hidden="true">
          <rect x="2" y="6" width="18" height="11" fill="var(--leaf)"/>
          <path d="M2 6 L11 13 L20 6" fill="none" stroke="#fff" stroke-width="1.5"/>
        </svg>
        daniel@harrowcrestbuilders.com.au
      </li>
      <li>
        <svg class="contact-icon" viewBox="0 0 22 22" aria-hidden="true" fill="none" stroke="var(--leaf)" stroke-width="1.3">
          <circle cx="11" cy="11" r="8.5"/>
          <ellipse cx="11" cy="11" rx="3.8" ry="8.5"/>
          <line x1="2.5" y1="11" x2="19.5" y2="11"/>
          <path d="M4 6.5 H18 M4 15.5 H18"/>
        </svg>
        www.harrowcrestbuilders.com.au
      </li>
      <li>
        <svg class="contact-icon" viewBox="0 0 22 22" aria-hidden="true">
          <path d="M11 2 C7 2 5 5 5 8 C5 12 11 20 11 20 C11 20 17 12 17 8 C17 5 15 2 11 2 Z" fill="var(--leaf)"/>
          <circle cx="11" cy="8" r="2.3" fill="#fff"/>
        </svg>
        PO Box 4172 Northgate LPO Bellfield WA 6091
      </li>
    </ul>

    <p class="registration">Registration 40817 ABN: 52 904 316 278</p>
  </section>

  <section class="card card-back" aria-label="Business card back">
    <div class="brand brand-back">
      <span class="brand-mark"></span>
      <span class="brand-name">Harrow Crest Builders</span>
    </div>
  </section>
</main>
</body>
</html>
```